Volusion Pawbright Web Template

We need a new web design for an online Pawbright based in Australia but looking to expand internationally in the future.

The template HTML & CSS should be easily integrated into a volusion web-store.

We sell a wide range of high quality pet products to our customers at competitive prices.This is our unique selling point.

We intend to become a market leader hence our brand has to look the part with simple yet outstanding icons.

The overall design has to be more visually appealing and simpler than our competitors and lead to a higher conversion rate.

The following are our biggest competitors:
www.mossfold.com.au
www.grovewick.com.au
www.tidlowe.com.au

Of our competitors www.tidlowe.com.au has the feel that we intend to have but obviously it has to be unique & iconic.

In short our web design has to be associated with Leading,Trust & Quality.
Updates

Please find attached Logo so that the site color theme can blend with the logo.

Target Market(s)

Online Pet Products shoppers worldwide

Industry/Entity Type

Pet

Coding

Coded - Design and coding required

Number of Pages Required

3 page

Font styles to use
Sans Serif

Requirements
Must have
• Check out page design.
• Product description menus(when you click on the product)
• Categories should be the same and should be hid or un-hidden by admin.
• Color theme will depend on the final logo to be completed soon.
Nice to have
• Please find attached logo.The site should blend well with logo.

```html
<!DOCTYPE html>
<html lang="en">
<head>
<meta charset="utf-8">
<title>Pawbright – Online Pet Supplies</title>
<link rel="stylesheet" href="https://fonts.googleapis.com/css2?family=Open+Sans:wght@400;600;700&family=Noto+Serif&family=Roboto+Condensed:wght@700&display=swap">
<style>
:root{
  --teal:#3da68f;
  --teal-dark:#2f8f79;
  --teal-text:#3a9e88;
  --pink:#f79ac0;
  --pink-strong:#f0679b;
  --blue:#0f78b8;
  --green:#8fd15a;
  --red:#d7202a;
  --navy:#1f4f8a;
  --grey-bg:#e6e6e6;
  --footer-dark:#2b2d33;
  --text:#555;
  --line:#e3e3e3;
}
*{box-sizing:border-box;margin:0;padding:0}
html,body{width:1200px;height:2230px;overflow:hidden}
body{position:relative;background:#fff;font-family:"Open Sans",Arial,sans-serif;color:var(--text)}
a{color:inherit;text-decoration:none}

/* header */
.site-header{position:absolute;left:0;top:0;width:1200px;height:178px;background:var(--teal);overflow:hidden}
.brand{position:absolute;left:85px;top:-30px;width:240px;height:240px;border-radius:50%;background:var(--teal-dark);border:6px solid #58b8a2;display:flex;align-items:center;justify-content:center;gap:10px}
.brand-dot{width:22px;height:22px;border-radius:50%;background:#fff}
.brand-name{font-weight:700;font-size:30px;color:#fff;letter-spacing:1px}
.top-links{position:absolute;left:382px;top:12px;height:20px;display:flex;gap:19px;font-size:14px;color:#fff;white-space:nowrap}
.top-links a{display:flex;align-items:center;gap:8px}
.top-links a::before{content:"";width:6px;height:6px;border-radius:50%;background:#1e6e5d}
.search{position:absolute;left:874px;top:4px;width:243px;height:36px;display:flex}
.search input{flex:1;border:0;font:italic 13px "Open Sans",sans-serif;padding:0 12px;color:#666}
.search button{width:38px;border:0;background:var(--pink-strong);display:flex;align-items:center;justify-content:center}
.cart-pet{position:absolute;left:855px;top:58px;width:82px;height:62px;background:linear-gradient(#e3a56a,#c57a3d);border-radius:40% 40% 8px 8px}
.cart-title{position:absolute;left:975px;top:82px;display:flex;align-items:center;gap:8px;color:#fff;font-size:16px;font-weight:600}
.cart-box{position:absolute;left:837px;top:124px;width:280px;height:36px;background:#fff;border-radius:3px;display:flex;align-items:center;padding:0 9px;font-size:13px;color:#444;gap:8px;white-space:nowrap}
.pill{border-radius:12px;color:#fff;font-size:13px;padding:2px 14px;font-weight:600}
.pill.view{background:var(--pink-strong)}
.pill.checkout{background:var(--teal)}

/* nav */
.main-nav{position:absolute;left:83px;top:178px;width:1034px;height:57px;display:flex;justify-content:space-between;padding-right:32px;font-family:"Noto Serif",Georgia,serif;font-size:14px;color:#666;white-space:nowrap}
.main-nav a{display:flex;align-items:center;letter-spacing:.3px}
.main-nav a.active{background:#f6b7cf;color:#333;padding:0 16px}

/* hero */
.hero{position:absolute;left:83px;top:235px;width:1034px;height:451px;overflow:hidden;background:linear-gradient(90deg,#c8dbe2 0%,#d7e7ea 40%,#eef0ea 70%,#f2efe6 100%)}
.hero-photo{position:absolute;left:0;top:0;width:700px;height:451px;background:radial-gradient(ellipse at 35% 45%,#c9782f 0%,#b4661f 35%,rgba(200,140,80,0) 70%)}
.hero-circle{position:absolute;left:690px;top:0;width:430px;height:430px;border-radius:50%;background:#fff;border:18px solid rgba(255,255,255,.55);background-clip:padding-box;display:flex;flex-direction:column;justify-content:center;padding-left:70px;color:var(--teal-text);font-weight:700;font-size:96px;line-height:.98}
.hero-copy{position:absolute;left:492px;top:312px;font-family:"Roboto Condensed",sans-serif;font-weight:700;font-size:36px;line-height:1.02;color:#111}
.shop-now{position:absolute;left:578px;top:406px;font-family:"Roboto Condensed",sans-serif;font-weight:700;font-size:19px;color:#111;padding:2px 10px;border:2px solid #111;border-top:0}

/* promos */
.promo{position:absolute;top:712px;width:504px;height:226px;overflow:hidden}
.promo-left{left:83px;background:#fdb9d3}
.promo-right{left:613px;background:linear-gradient(90deg,#0c6fa8,#0e86c0)}
.promo-art{position:absolute;left:0;top:0;width:250px;height:226px}
.promo-left .promo-art{background:linear-gradient(160deg,#f9cfe0,#e7a2b8 60%,#d46b82)}
.promo-right .promo-art{background:radial-gradient(ellipse at 55% 55%,#f0c040 0%,#d4a030 25%,#0a6aa0 60%)}
.sale-badge{position:absolute;left:305px;top:25px;width:106px;height:106px;border-radius:50%;background:#f27aa5;border:5px solid #fdd4e3;color:#fff;text-align:center;font-weight:700;font-size:34px;line-height:1;padding-top:14px}
.sale-badge small{display:block;font-size:22px;font-style:italic;font-weight:600}
.promo-left .promo-title{position:absolute;left:252px;top:138px;color:#fff;font-weight:700;font-size:27px;line-height:1.2;text-align:center;width:220px}
.promo-right .promo-title{position:absolute;left:275px;top:38px;color:#fff;font-weight:700;font-size:27px;line-height:1.12}
.promo-right .promo-title em{display:block;font-style:normal;color:#7ee0d0;font-size:38px;margin-bottom:10px}
.promo-right .promo-title span{color:#d8f2ff}
.promo-arrow{position:absolute;right:-18px;top:88px;width:48px;height:48px;border-radius:50%;background:#fff;display:flex;align-items:center;padding-left:10px}

/* products */
.products{position:absolute;left:83px;top:967px;width:1034px;display:grid;grid-template-columns:repeat(4,237px);column-gap:29px;row-gap:30px}
.card{height:343px;border:1px solid #ececec;box-shadow:0 1px 4px rgba(0,0,0,.12);background:#fff;position:relative}
.card-media{height:218px;border-bottom:1px solid var(--line);display:flex;align-items:center;justify-content:center}
.card-media .shot{width:150px;height:170px;border-radius:10px}
.shot.carrier{background:linear-gradient(#d8c9a0,#b89a5c)}
.shot.dental{background:linear-gradient(#e9514f,#2aa7c9);width:110px}
.shot.wipes{background:linear-gradient(#f8c03a,#ef8d1c)}
.shot.robe{background:linear-gradient(#c4a4e0,#8f63c3)}
.shot.crate{background:linear-gradient(#5ac48a,#3a3a3a)}
.shot.bed{background:linear-gradient(#7a2a62,#4c173d);width:130px}
.stars{position:absolute;right:12px;top:8px;color:#e0303a;font-size:10px;letter-spacing:-1px}
.card-name{margin:13px 0 0 18px;color:var(--teal-text);font-size:18px;font-weight:600;letter-spacing:.3px;white-space:nowrap}
.card-desc{margin:4px 0 0 18px;font-size:13px;color:#666}
.card-buy{position:absolute;left:18px;right:20px;bottom:18px;display:flex;align-items:center;justify-content:space-between}
.price{color:var(--navy);font-weight:600;font-size:19px}
.add-cart{background:var(--red);color:#fff;font-size:12px;font-weight:600;width:113px;height:33px;display:flex;align-items:center;justify-content:center;border-radius:2px}

/* features */
.feature{position:absolute;top:1714px;width:320px;height:140px;display:flex;align-items:center;gap:14px;padding-left:14px;color:#fff;white-space:nowrap}
.feature h3{font-size:26px;font-weight:700;line-height:1.05}
.feature p{font-size:15px;font-weight:600}
.f-ship{left:83px;background:var(--pink)}
.f-order{left:440px;background:var(--green)}
.f-card{left:797px;background:var(--blue)}

/* footer */
.site-footer{position:absolute;left:0;top:1891px;width:1200px;height:271px;background:var(--grey-bg)}
.f-col{position:absolute;top:35px}
.f-col h4{color:#1e6aa8;font-size:16px;font-weight:600;margin-bottom:14px}
.f-col li{list-style:none;font-size:13px;color:#666;height:31px;display:flex;align-items:center;gap:10px}
.f-col.links li::before{content:"";width:7px;height:7px;border:1px solid #999}
.soc{width:16px;height:16px;border-radius:50%;background:#444}
.f-col.social li:first-child .soc{background:#1f5fa8}
.f-col.social li:first-child{color:#1e6aa8}
.f-col.contact li{height:auto;align-items:flex-start;margin-bottom:18px;line-height:1.5}
.bottom-bar{position:absolute;left:0;top:2162px;width:1200px;height:68px;background:var(--footer-dark);color:#999;font-size:13px;display:flex;align-items:center;padding:0 83px;justify-content:space-between}
.pay{display:flex;gap:7px}
.pay span{background:#eee;color:#333;font-size:10px;font-weight:700;border-radius:3px;width:52px;height:25px;display:flex;align-items:center;justify-content:center}
</style>
</head>
<body>

<header class="site-header">
  <div class="brand"><span class="brand-dot"></span><span class="brand-name">PAWBRIGHT</span></div>
  <nav class="top-links"><a href="#">My Account</a><a href="#">My Wishlist</a><a href="#">My Cart</a><a href="#">Checkout</a><a href="#">Log In</a></nav>
  <form class="search"><input type="text" placeholder="Search..." value="Search..."><button type="button" aria-label="Search"><svg width="16" height="16" viewBox="0 0 16 16"><circle cx="6.5" cy="6.5" r="5" fill="none" stroke="#fff" stroke-width="2"/><line x1="10" y1="10" x2="15" y2="15" stroke="#fff" stroke-width="2"/></svg></button></form>
  <div class="cart-pet" role="img" aria-label="Small dog sitting beside the cart"></div>
  <div class="cart-title"><svg width="34" height="24" viewBox="0 0 34 24"><path d="M1 3h6l4 13h17l4-10H10" fill="none" stroke="#fff" stroke-width="2.4"/><circle cx="13" cy="21" r="2" fill="#fff"/><circle cx="26" cy="21" r="2" fill="#fff"/></svg>Shopping cart</div>
  <div class="cart-box">$0.00 (0 items) <span class="pill view">View</span><span class="pill checkout">Chechkout</span></div>
</header>

<nav class="main-nav">
  <a class="active" href="#">HOME</a><a href="#">ABOUT US</a><a href="#">DOG</a><a href="#">CAT</a><a href="#">FISH</a><a href="#">REPTILE</a><a href="#">SMALL ANIMAL</a><a href="#">BIRD</a><a href="#">HORSE</a><a href="#">CHICKEN</a><a href="#">CONTACT US</a>
</nav>

<section class="hero">
  <div class="hero-photo" role="img" aria-label="Golden retriever panting on a sunny beach"></div>
  <div class="hero-circle">50%<br>OFF</div>
  <div class="hero-copy">VITAMINS &amp;<br>SUPPLEMENTS</div>
  <a class="shop-now" href="#">SHOP NOW</a>
</section>

<section class="promo promo-left">
  <div class="promo-art" role="img" aria-label="Small terrier in a pink dress with flowers"></div>
  <div class="sale-badge"><small>final</small>SALE</div>
  <div class="promo-title">Dog Clothing &amp;<br>Accessories</div>
  <span class="promo-arrow"><svg width="12" height="18" viewBox="0 0 12 18"><path d="M2 2l7 7-7 7" fill="none" stroke="#aaa" stroke-width="2.5"/></svg></span>
</section>
<section class="promo promo-right">
  <div class="promo-art" role="img" aria-label="Yellow tropical fish over coral"></div>
  <div class="promo-title"><em>New!</em><span>Natural<br>LED Aquarium<br>Lighting</span></div>
  <span class="promo-arrow"><svg width="12" height="18" viewBox="0 0 12 18"><path d="M2 2l7 7-7 7" fill="none" stroke="#aaa" stroke-width="2.5"/></svg></span>
</section>

<section class="products">
  <article class="card"><span class="stars">★★★★★</span><div class="card-media"><div class="shot carrier" role="img" aria-label="Woven pet carrier bag with small dog"></div></div><h3 class="card-name">PET CARRIER</h3><p class="card-desc">Lorem ipsum dolor sit amet</p><div class="card-buy"><span class="price">$ 98.00</span><a class="add-cart" href="#">ADD TO CART</a></div></article>
  <article class="card"><div class="card-media"><div class="shot dental" role="img" aria-label="Dental cleaning pads pack"></div></div><h3 class="card-name">DENTAROO CARE</h3><p class="card-desc">Lorem ipsum dolor sit amet</p><div class="card-buy"><span class="price">$ 98.00</span><a class="add-cart" href="#">ADD TO CART</a></div></article>
  <article class="card"><div class="card-media"><div class="shot wipes" role="img" aria-label="Bath wipes packs"></div></div><h3 class="card-name">FRESHENING SPRAYS</h3><p class="card-desc">Lorem ipsum dolor sit amet</p><div class="card-buy"><span class="price">$ 98.00</span><a class="add-cart" href="#">ADD TO CART</a></div></article>
  <article class="card"><div class="card-media"><div class="shot robe" role="img" aria-label="Small dog in a purple bath robe"></div></div><h3 class="card-name">BATH ROBE</h3><p class="card-desc">Lorem ipsum dolor sit amet</p><div class="card-buy"><span class="price">$ 98.00</span><a class="add-cart" href="#">ADD TO CART</a></div></article>
  <article class="card"><div class="card-media"><div class="shot crate" role="img" aria-label="Plastic pet crate with small dog"></div></div><h3 class="card-name">DENIM BAG</h3><p class="card-desc">Lorem ipsum dolor sit amet</p><div class="card-buy"><span class="price">$ 98.00</span><a class="add-cart" href="#">ADD TO CART</a></div></article>
  <article class="card"><div class="card-media"><div class="shot bed" role="img" aria-label="Purple cave style pet bed"></div></div><h3 class="card-name">BATH ROBE</h3><p class="card-desc">Lorem ipsum dolor sit amet</p><div class="card-buy"><span class="price">$ 98.00</span><a class="add-cart" href="#">ADD TO CART</a></div></article>
  <article class="card"><div class="card-media"><div class="shot wipes" role="img" aria-label="Bath wipes packs"></div></div><h3 class="card-name">FRESHENING SPRAYS</h3><p class="card-desc">Lorem ipsum dolor sit amet</p><div class="card-buy"><span class="price">$ 98.00</span><a class="add-cart" href="#">ADD TO CART</a></div></article>
  <article class="card"><div class="card-media"><div class="shot carrier" role="img" aria-label="Woven pet carrier bag with small dog"></div></div><h3 class="card-name">BATH ROBE</h3><p class="card-desc">Lorem ipsum dolor sit amet</p><div class="card-buy"><span class="price">$ 98.00</span><a class="add-cart" href="#">ADD TO CART</a></div></article>
</section>

<div class="feature f-ship">
  <svg width="70" height="70" viewBox="0 0 70 70" fill="none" stroke="#fff" stroke-width="4"><rect x="10" y="8" width="50" height="44" rx="6"/><line x1="10" y1="30" x2="60" y2="30"/><line x1="4" y1="24" x2="10" y2="24"/><line x1="60" y1="24" x2="66" y2="24"/><rect x="16" y="52" width="10" height="10"/><rect x="44" y="52" width="10" height="10"/><circle cx="20" cy="42" r="3" fill="#fff"/><circle cx="50" cy="42" r="3" fill="#fff"/></svg>
  <div><h3>FREE SHIPPING</h3><p>ON ORDERS OVER $500</p></div>
</div>
<div class="feature f-order">
  <svg width="70" height="70" viewBox="0 0 70 70"><path d="M14 12c-8 8-6 22 8 36s28 16 36 8l-10-10-8 6C32 48 22 38 20 30l6-8z" fill="#fff"/><text x="32" y="38" fill="#fff" font-family="Open Sans,sans-serif" font-weight="700" font-size="18">24</text><path d="M30 14a24 24 0 0 1 30 14" fill="none" stroke="#fff" stroke-width="3" stroke-dasharray="4 4"/></svg>
  <div><h3>ORDER ONLINE</h3><p>HOURS: 8AM TO 11AM</p></div>
</div>
<div class="feature f-card">
  <svg width="70" height="70" viewBox="0 0 70 70" fill="none" stroke="#fff" stroke-width="4"><rect x="4" y="14" width="62" height="42" rx="4"/><line x1="4" y1="26" x2="66" y2="26"/><line x1="14" y1="38" x2="34" y2="38"/><line x1="14" y1="46" x2="26" y2="46"/></svg>
  <div><h3>SPECIAL CARDS</h3><p>GIVE THE PERFECT GIFT</p></div>
</div>

<footer class="site-footer">
  <div class="f-col links" style="left:83px"><h4>INFORMATION</h4><ul><li>Specials</li><li>New products</li><li>Best sellers</li><li>Our stores</li><li>Contact us</li><li>Pages configuration</li></ul></div>
  <div class="f-col links" style="left:360px"><h4>MY ACCOUNT</h4><ul><li>My orders</li><li>My merchandise returns</li><li>My credit slips</li><li>My addresses</li><li>My personal info</li><li>My vouchers</li></ul></div>
  <div class="f-col social" style="left:666px"><h4>FOLLOW US</h4><ul><li><span class="soc"></span>Chatterly</li><li><span class="soc"></span>Chirpwave</li><li><span class="soc"></span>Linkmoor</li><li><span class="soc"></span>Viewtide</li><li><span class="soc"></span>Orbitly</li></ul></div>
  <div class="f-col contact" style="left:901px"><h4>CONTACT US</h4><ul>
    <li><svg width="20" height="20" viewBox="0 0 20 20"><path d="M10 2a5 5 0 0 0-5 5c0 4 5 9 5 9s5-5 5-9a5 5 0 0 0-5-5z" fill="none" stroke="#999" stroke-width="1.5"/><circle cx="10" cy="7" r="1.8" fill="#999"/></svg>1234 street name, City Name,<br>States Name</li>
    <li><svg width="20" height="20" viewBox="0 0 20 20"><path d="M5 3c-3 3-2 7 3 11s8 4 10 2l-3-3-3 2c-2-1-4-3-5-5l2-3z" fill="#999"/></svg>123.456.7890</li>
    <li><svg width="20" height="20" viewBox="0 0 20 20" fill="none" stroke="#999" stroke-width="1.5"><rect x="2" y="5" width="16" height="11"/><path d="M2 5l8 6 8-6"/></svg>info@pawbright.com</li>
  </ul></div>
</footer>

<div class="bottom-bar">
  <span>© 2014 Pawbright. All right reserved.</span>
  <div class="pay"><span>Kardo</span><span>Vexa</span><span>Amberline</span><span>Meso</span><span>Cirro</span><span>Paywise</span></div>
</div>

</body>
</html>
```